Brochure, website and corporate stationary Design Project

Project scope:
1 x brochure (A4 insert) design
1 x brochure folder design (both external pages and one internal (there will be a few lines of text on the left inside page). The internal right side page will be a pocket for brochures (A4 inserts)
1 x corporate stationary pack (Business Card, logo (a proper logo file format needs to be produced), Letterhead and Envelope)
1 x concept design for our website. You dont need to do the coding. What you need to deliver is the design in a standard format (i.e. photoshop or blend)
Summary: the scope of the project is to design our brochure and its brochure folder, corporate stationary design and graphics concept design for our website. You should also consider our existing logo when performing the above design work (you can modify the logo slightly if you think it would improve look and feel and relevancy to overall design).
• We are a small IT services company
• The folder will be used to hold the brochures (inserts). The folder will be given to prospect customers (see attached a sample service brochure called “Fjällux User support services Ver0.1.docx”)
• On the cover of the folder, we want to have a design that uses keywords / phrases that reflects our main services (see attached file called “Phrases for presentation folder.docs”). Please note that not all phrases have to be used, use a logic in which ones or add new suggestions
• Inside the folder, at left side we want to have a short text explaining about our services a bit (see attached file called “Brochure Main section v0.91.docx”)
• All designs (corporate stationary, brochure, folder, web, etc.) must be consistent with each other and follow same concept, colour scheme, etc
• you are allowed to do minor changes to our existing logo if you have good reason to do so (see attached logo)
• We want our website design to be simple, elegant, not very colourful, light. HTML5. No flash. (you dont need to do the actual coding of the website, just deliver the design in Photoshop, Blend or any other standard format) With minimal menu items such as: home, services, about us, news, contact us, and other important ones if any. Same colour and design scheme as corporate stationary and brochures
• The company name “Fjällux” is derived from the Swedish word “Grön” (meaning green) and “teQ” which stands for technology but spelled with a “Q” to resemble Quality. The corporate green colour comes from the word “Grön”.
• All templates must be delivered in a standard editable format
Reason: To provide more time to the designers to come with their design submissions.
please note that we more than doubled the budget for this project
We deliver IT services to companies of 3-4 employees upto 200-300 employees. The brochures are intended for prospect customers (non IT people)
Business

```html
<!DOCTYPE html>
<html lang="en">
<head>
<meta charset="utf-8">
<title>Fjällux – Folder Spread</title>
<link rel="stylesheet" href="https://fonts.googleapis.com/css2?family=Fira+Sans:wght@400;500&display=swap">
<style>
  :root {
    --backdrop: #33393c;
    --paper: #f3f3f3;
    --slate: #687071;
    --brand-green: #8cc63f;
    --ink-dark: #2e2b2c;
    --ink-heading: #666a6b;
    --ink-body: #7a7d7e;
    --ink-logo: #3b3b3b;
  }
  * { margin: 0; padding: 0; box-sizing: border-box; }
  html, body {
    width: 1200px; height: 1126px; overflow: hidden;
    background: var(--backdrop);
    font-family: "Fira Sans", Arial, sans-serif;
  }
  .folder-spread {
    position: absolute; left: 32px; top: 162px;
    width: 1136px; height: 802px;
    box-shadow: 0 8px 30px rgba(0,0,0,.4);
  }
  .inside-left {
    position: absolute; left: 0; top: 0; width: 568px; height: 802px;
    background: var(--paper); overflow: hidden;
  }
  .inside-right {
    position: absolute; left: 568px; top: 0; width: 568px; height: 802px;
    background: var(--slate);
  }
  .pocket { position: absolute; left: 0; top: 0; width: 568px; height: 802px; }
  .page-title {
    position: absolute; left: 26px; top: 250px;
    font-size: 18px; font-weight: 400; color: var(--ink-heading);
  }
  .text-column {
    position: absolute; top: 254px; width: 188px;
    font-size: 8.6px; line-height: 11.4px; color: var(--ink-body);
  }
  .text-column.intro { left: 150px; }
  .text-column.services-detail { left: 356px; }
  .text-column p { margin-bottom: 11.4px; }
  .section-label {
    color: var(--brand-green); font-weight: 500; text-transform: uppercase;
    font-size: 8.6px; margin-bottom: 0;
  }
  .section-label.spaced { margin-top: 4px; }
  .lifecycle .step-arrow { color: var(--brand-green); font-weight: 500; }
  .service-list { list-style: none; }
  .service-list li { position: relative; padding-left: 6px; }
  .service-list li::before {
    content: ""; position: absolute; left: 0; top: 4px;
    width: 4px; height: 4px; border-radius: 50%; background: var(--brand-green);
  }
  .brand-name {
    position: absolute; left: 356px; top: 684px;
    font-size: 31px; font-weight: 500; letter-spacing: 1.5px;
    color: var(--ink-logo); text-transform: uppercase;
  }
  .brand-url {
    position: absolute; left: 356px; top: 724px;
    font-size: 7.5px; font-weight: 500; color: var(--ink-logo);
  }
  .footer-band {
    position: absolute; left: 0; bottom: 0; width: 568px; height: 27px;
    background: var(--ink-dark);
  }
  .footer-accent {
    position: absolute; left: 37px; bottom: 0; width: 65px; height: 27px;
    background: var(--brand-green);
  }
</style>
</head>
<body>
  <main class="folder-spread">
    <section class="inside-left">
      <h1 class="page-title">About us</h1>

      <div class="text-column intro">
        <h2 class="section-label">Introduction</h2>
        <p>Fjällux is a prominent information technology management consultancy headquartered in Dubai, providing services across the GCC region.</p>
        <p>We work in a unique way by partnering with clients and acting as a trusted advisor for their management team. We provide business leaders with high-quality, up to date and expert strategic advice to help them make informed decisions about their organisations technology investments.</p>
        <p>We cover the entire lifecycle of IT service delivery</p>
        <p class="lifecycle">Management Consultancy <span class="step-arrow">›</span> Solution Design <span class="step-arrow">›</span> Solution Delivery <span class="step-arrow">›</span> Ongoing Support</p>
        <h2 class="section-label spaced">Services</h2>
      </div>

      <div class="text-column services-detail">
        <p>Our services include the entire range of technology solutions for small, medium and large businesses.</p>
        <p>We offer strategy and business change advice, systems integration and managed services for infrastructure, applications, cyber security, and development of web and mobile software applications.</p>
        <p>To offer such comprehensive services we have handpicked partners that are the best in their field at what they do be it software development, security audit or data centre setup. This approach allows us to add exceptional quality and depth to our services while eliminating the need for clients to deal with multiple vendors.</p>
        <p>Whether you are a start-up or an established company we have the right range of services for you.<br>These include:</p>
        <ul class="service-list">
          <li>IT Management and Consultancy</li>
          <li>Server, Telephony and Network Installation and Support</li>
          <li>User Support</li>
          <li>Cloud Services - Email, Storage, Business Applications</li>
          <li>Security</li>
          <li>Business Applications (CRM, ERP, Accounting software)</li>
          <li>App Development</li>
        </ul>
      </div>

      <div class="brand-name">Fjällux</div>
      <div class="brand-url">www.fjallux.com</div>

      <div class="footer-band"></div>
      <div class="footer-accent"></div>
    </section>

    <section class="inside-right">
      <svg class="pocket" viewBox="0 0 568 802" aria-hidden="true">
        <polygon points="45,515 568,515 568,802 8,802" fill="var(--brand-green)" stroke="#ffffff" stroke-width="1.5"/>
      </svg>
    </section>
  </main>
</body>
</html>
```